Design a Professional Business Card for Velmora Arcs

Design a business card for Velmora Arcs, we are a National Sport Court Company.

West Region Address: 4175 Quill Harbor Ln, Suite #215 Englewood, Colorado 80467
East Region Address: 3817 Tamsin Rd E, Bradenton, Florida 34583

Target Market(s)

High End Residential & Institutional Clients

Industry/Entity Type

Design & Construction

Contact Information for Business Card

Logo/Brand/Colors/ name, number (provided in comments)

Requirements
Must have
• Colors only provided in logo
Should not have
• Any other colors not in existing logo (attached)

```html
<!DOCTYPE html>
<html lang="en">
<head>
<meta charset="utf-8">
<title>Velmora Arcs – Business Card</title>
<link href="https://fonts.googleapis.com/css2?family=Carlito:wght@400;700&display=swap" rel="stylesheet">
<style>
  :root {
    --brand-blue: #001a80;
    --brand-green: #127a05;
    --ink: #1a1a1a;
    --paper: #ffffff;
    --backdrop: #e3e3e3;
  }
  * { margin: 0; padding: 0; box-sizing: border-box; }
  html, body {
    width: 1200px; height: 1200px; overflow: hidden;
    background: var(--backdrop);
    font-family: "Carlito", "Calibri", sans-serif;
  }
  .card {
    position: absolute; left: 344px; width: 514px; height: 285px;
    border-radius: 31px; overflow: hidden;
  }
  .card--front { top: 295px; background: var(--paper); border: 1.5px solid var(--ink); }
  .card--back { top: 625px; background: var(--brand-blue); }

  .brand { position: absolute; display: flex; align-items: center; gap: 12px; }
  .brand__dot { width: 62px; height: 62px; border-radius: 50%; background: var(--brand-green); flex: none; }
  .brand__name {
    font-weight: 700; font-size: 29px; line-height: 27px;
    letter-spacing: 2px; text-transform: uppercase;
  }
  .card--front .brand { left: 18px; top: 111px; }
  .card--front .brand__name { color: var(--brand-blue); }
  .card--back .brand { left: 147px; top: 106px; }
  .card--back .brand__name { color: var(--paper); }

  .divider { position: absolute; left: 256px; top: 63px; width: 1.5px; height: 141px; background: var(--brand-blue); }

  .person { position: absolute; left: 268px; top: 39px; }
  .person__name { font-weight: 700; font-size: 28px; line-height: 32px; color: var(--ink); }
  .person__name .given { color: var(--brand-blue); }
  .person__title { font-size: 20px; line-height: 24px; color: var(--ink); }

  .contacts { position: absolute; left: 268px; top: 103px; list-style: none; }
  .contacts li { display: flex; align-items: center; height: 31px; font-size: 17.5px; color: var(--ink); }
  .contacts svg { width: 14px; height: 14px; margin-right: 7px; fill: var(--brand-blue); flex: none; }

  .addresses {
    position: absolute; left: 0; right: 0; top: 206px;
    text-align: center; font-weight: 700; font-size: 12.2px; line-height: 17px; color: var(--ink);
  }

  .band { position: absolute; left: 0; bottom: 0; width: 100%; height: 32px; }
  .band--blue { background: var(--brand-blue); }
  .band--green { background: var(--brand-green); }
  .band svg { position: absolute; left: 0; top: 0; }

  .website {
    position: absolute; left: 148px; top: 193px;
    display: flex; align-items: center;
    color: var(--paper); font-weight: 700; font-size: 13px; letter-spacing: 3.4px;
  }
  .website svg { width: 12px; height: 12px; margin-right: 6px; }
</style>
</head>
<body>

<section class="card card--front">
  <div class="brand">
    <span class="brand__dot"></span>
    <span class="brand__name">Velmora<br>Arcs</span>
  </div>

  <span class="divider"></span>

  <div class="person">
    <h1 class="person__name"><span class="given">Dorian V.</span> Ashcombe</h1>
    <p class="person__title">CEO &amp; Founder</p>
  </div>

  <ul class="contacts">
    <li>
      <svg viewBox="0 0 14 14"><circle cx="7" cy="3.5" r="3"/><path d="M1 14v-2.5C1 9 3.5 7.5 7 7.5s6 1.5 6 4V14z"/></svg>
      (303) 555-0147
    </li>
    <li>
      <svg viewBox="0 0 14 14"><rect x="3" y="0" width="8" height="14" rx="1.5"/><rect x="6" y="11" width="2" height="1.2" fill="#fff"/></svg>
      1-800-555-0193
    </li>
    <li>
      <svg viewBox="0 0 14 14"><path d="M0 2h14v10H0z"/><path d="M1.5 3.5L7 8l5.5-4.5" stroke="#fff" stroke-width="1.4" fill="none"/></svg>
      dorian@velmoraarcs.com
    </li>
  </ul>

  <p class="addresses">
    West Region Address: 4175 Quill Harbor Ln, Suite #215 Englewood, Colorado 80467<br>
    East Region Address: 3817 Tamsin Rd E, Bradenton, Florida 34583
  </p>

  <div class="band band--blue">
    <svg width="514" height="32" viewBox="0 0 514 32">
      <polygon points="173,0 184,0 197,32 187,32" fill="var(--paper)"/>
      <polygon points="204,0 215,0 229,32 218,32" fill="var(--paper)"/>
    </svg>
  </div>
</section>

<section class="card card--back">
  <div class="brand">
    <span class="brand__dot"></span>
    <span class="brand__name">Velmora<br>Arcs</span>
  </div>

  <p class="website">
    <svg viewBox="0 0 12 12" fill="none" stroke="#fff" stroke-width="1.2"><circle cx="6" cy="6" r="5.2"/><path d="M0.8 6h10.4M6 0.8c-2.2 3-2.2 7.4 0 10.4M6 0.8c2.2 3 2.2 7.4 0 10.4"/></svg>
    www.velmoraarcs.com
  </p>

  <div class="band band--green">
    <svg width="514" height="32" viewBox="0 0 514 32">
      <polygon points="173,0 184,0 197,32 187,32" fill="var(--brand-blue)"/>
      <polygon points="204,0 215,0 229,32 218,32" fill="var(--brand-blue)"/>
    </svg>
  </div>
</section>

</body>
</html>
```